Tombo's Pan. Chicken shop

yDesign special menu with special pictures within 48 h
Very smaple menu

Target Market(s)

Local

Industry/Entity Type

Food

Colors
FFF300
FFF600
FEFA6F
FFFEC7
FFFEE8

Requirements
Must have
• IGood quality picture
Nice to have
• Good quality pictures

```html
<!DOCTYPE html>
<html lang="en">
<head>
<meta charset="utf-8">
<title>Tombo's Pan – Menu</title>
<link href="https://fonts.googleapis.com/css2?family=Exo+2:wght@400;600;700;900&display=swap" rel="stylesheet">
<style>
  :root{
    --yellow:#FFF300;
    --yellow-soft:#FEFA6F;
    --ink:#0b0b0b;
    --panel:#111111;
    --text:#f2f2f2;
    --divider:#bdbdbd;
  }
  *{margin:0;padding:0;box-sizing:border-box}
  html,body{width:1200px;height:848px;overflow:hidden;background:var(--yellow)}
  body{font-family:"Exo 2",sans-serif;color:var(--text)}
  .menu{position:relative;width:1200px;height:848px;background:var(--yellow);overflow:hidden}

  .masthead{position:absolute;left:0;top:0;width:1200px;height:188px;display:flex;align-items:center;justify-content:center}
  .brand-name{font-family:"Exo 2",sans-serif;font-weight:900;font-size:118px;line-height:1;color:var(--ink);text-transform:uppercase;letter-spacing:2px;margin-top:-6px}

  .board{position:absolute;left:0;top:188px;width:1200px;height:599px;background:var(--panel)}
  .scallop-top{position:absolute;left:0;top:184px;width:1200px;height:8px;
    background:radial-gradient(circle at 5px 0,var(--yellow) 4.5px,transparent 5px) repeat-x;background-size:10px 8px}
  .scallop-bottom{position:absolute;left:0;top:781px;width:1200px;height:8px;
    background:radial-gradient(circle at 5px 8px,var(--yellow) 4.5px,transparent 5px) repeat-x;background-size:10px 8px}

  .divider{position:absolute;top:192px;height:591px;border-left:1px dashed var(--divider)}

  .col{position:absolute;top:0;height:848px;z-index:2}
  .block{position:absolute;left:0;width:225px}
  .col-title{position:absolute;text-align:center;color:var(--yellow);font-weight:700;font-size:21px;line-height:26px;text-transform:uppercase;letter-spacing:.3px}
  .col-note{position:absolute;text-align:center;font-size:9.5px;line-height:13px;color:var(--text)}
  .step{color:var(--yellow);font-weight:700;font-size:14px;line-height:20px}
  .line{font-size:9.8px;line-height:17.6px;white-space:nowrap}
  .label{display:inline-block}
  .price{color:var(--yellow)}
  .item{color:var(--yellow);font-weight:700;font-size:16.5px;line-height:20px;white-space:nowrap}
  .side{color:var(--yellow);font-weight:700;font-size:13.5px;line-height:20px;white-space:nowrap}
  .desc{font-size:9.8px;line-height:17.6px}
  .desc.tight{line-height:13px}

  .photo{position:absolute;z-index:1}
</style>
</head>
<body>
<main class="menu">
  <header class="masthead">
    <h1 class="brand-name">Tombo's Pan</h1>
  </header>

  <div class="board"></div>
  <div class="scallop-top"></div>
  <div class="scallop-bottom"></div>

  <div class="divider" style="left:238px"></div>
  <div class="divider" style="left:478px"></div>
  <div class="divider" style="left:718px"></div>
  <div class="divider" style="left:959px"></div>

  <!-- Breaded wings -->
  <section class="col" style="left:25px;width:210px">
    <h2 class="col-title" style="left:-10px;width:212px;top:211px">Breaded Wings</h2>
    <p class="col-note" style="left:-10px;width:212px;top:239px">ALL WINGS SERVIED WITH FRIES &amp; 1 dip</p>
    <div class="block" style="top:295px">
      <h3 class="step">STEP 1</h3>
      <p class="line">Wings</p><p class="line">Boneless</p>
    </div>
    <div class="block" style="top:366px">
      <h3 class="step">STEP 2</h3>
      <p class="line"><span class="label" style="width:63px">4 wings</span><span class="price">6.99</span></p>
      <p class="line"><span class="label" style="width:63px">8 Wings</span><span class="price">9.75£</span></p>
      <p class="line"><span class="label" style="width:63px">10 wings</span><span class="price">11.50</span></p>
      <p class="line"><span class="label" style="width:63px">12 Wings</span><span class="price">12.95</span></p>
    </div>
    <div class="block" style="top:471px">
      <h3 class="step">STEP 3</h3>
      <p class="line">Choose your &nbsp;flavour</p>
      <p class="line">1 Original</p><p class="line">2 buffalo</p><p class="line">3 bbq</p>
      <p class="line">4 lemon paper</p><p class="line">5 garlic parmesan</p>
      <p class="line">6 dynamite</p><p class="line">7 Nashville oh hot damn</p>
    </div>
    <div class="block" style="top:647px">
      <h3 class="step">STEP 4</h3>
      <p class="line">Choose your sause</p><p class="line">Blue cheese</p>
      <p class="line">Honey mustard</p><p class="line">House ranch</p>
      <p class="line">Tombo's special</p>
    </div>
  </section>
  <div class="photo" role="img" aria-label="Breaded chicken wings on a board with dip" style="left:101px;top:270px;width:116px;height:111px;border-radius:10px;background:radial-gradient(circle at 45% 50%,#c9792a,#7a4a1c 60%,#4f7f2a)"></div>
  <div class="photo" role="img" aria-label="Golden fried chicken wings" style="left:125px;top:496px;width:110px;height:98px;border-radius:40%;background:radial-gradient(circle,#d39a45,#9a5f22 65%,transparent 72%)"></div>
  <div class="photo" role="img" aria-label="Grilled chicken piece" style="left:131px;top:668px;width:81px;height:100px;border-radius:40%;background:radial-gradient(circle,#8a4a22,#4a2612 65%,transparent 72%)"></div>
  <div class="photo" role="img" aria-label="Crispy chicken bites" style="left:41px;top:768px;width:160px;height:54px;border-radius:40%;background:radial-gradient(circle,#d48a3a,#a2561e 65%,transparent 72%)"></div>

  <!-- Buttermilk tenders -->
  <section class="col" style="left:253px;width:215px">
    <h2 class="col-title" style="left:-10px;width:235px;top:211px">Buttermilk<br>Marinated Tenders</h2>
    <p class="col-note" style="left:-10px;width:235px;top:265px">ALL Tenders SERVIED WITH FRIES &amp; 1 dip</p>
    <div class="block" style="top:295px">
      <h3 class="step">STEP 1</h3>
      <p class="line">Large</p><p class="line">Mini</p>
    </div>
    <div class="block" style="top:366px">
      <h3 class="step">STEP 2</h3>
      <p class="line"><span class="label" style="width:60px">3 &nbsp;tenders</span><span class="price">5.99£</span></p>
      <p class="line"><span class="label" style="width:60px">6 tenders</span><span class="price">8.99</span></p>
    </div>
    <div class="block" style="top:437px">
      <h3 class="step">STEP 3</h3>
      <p class="line">Choose your falvour</p>
      <p class="line">1 Original</p><p class="line">2 buffalo</p><p class="line">3 bbq</p>
      <p class="line">4 lemon paper</p><p class="line">5 garlic parmesan</p>
      <p class="line">6 dynamite</p><p class="line">7 Nashville oh hot damn</p>
    </div>
    <div class="block" style="top:612px">
      <h3 class="step">STEP 4</h3>
      <p class="line">Choose your sause</p><p class="line">Blue cheese</p>
      <p class="line">Honey mustard</p><p class="line">House ranch</p>
      <p class="line">Tombo's special</p>
    </div>
  </section>
  <div class="photo" role="img" aria-label="Bowl of creamy herb dip" style="left:349px;top:294px;width:111px;height:111px;border-radius:50%;background:radial-gradient(circle,#f4f4ee,#d9dcd2 60%,#a8aca4)"></div>
  <div class="photo" role="img" aria-label="Bowl of yoghurt topped with blueberries" style="left:354px;top:479px;width:103px;height:86px;border-radius:45%;background:radial-gradient(circle at 50% 40%,#ffffff,#e3e6ea 65%,transparent 72%)"></div>
  <div class="photo" role="img" aria-label="Dairy products: milk, cheese and butter" style="left:340px;top:700px;width:142px;height:134px;border-radius:12px;background:linear-gradient(100deg,#f1f1ec 0%,#e9e8e0 50%,#f2c94c 72%,#e7b93a 100%)"></div>

  <!-- Sandwich option 1 -->
  <section class="col" style="left:489px;width:225px">
    <h2 class="col-title" style="left:-4px;width:232px;top:211px">Sandwich Option 1</h2>
    <p class="col-note" style="left:-4px;width:232px;top:239px">All meals servived with chips and dip</p>
    <div class="block" style="top:295px;width:225px">
      <h3 class="item">1-Classic burger</h3>
      <p class="desc">Fried chicken breast, fresh pickles &amp; creamy<br>mayo in a soft brioche bun <span class="price">5.50</span></p>
    </div>
    <div class="block" style="top:369px;width:225px">
      <h3 class="item">2-Tombo's special</h3>
      <p class="desc">(Relish sauce, Fried chicken breast,Honey<br>mustard, Red cabbage in a soft brioche bun )<br><span class="price">6.95</span></p>
    </div>
    <div class="block" style="top:460px;width:225px">
      <h3 class="item">3- Nashville oh hot damn</h3>
      <p class="desc">Fried nashville chicken breast, fresh pickles &amp;<br>tombo's sause, pot of grave&amp; mash potato <span class="price">7.99</span></p>
    </div>
    <div class="block" style="top:533px;width:225px">
      <h3 class="item">5-Double cheesy toasted</h3>
      <p class="desc">( tenders ,Cheese, slaw, pickles, mayo) <span class="price">5.99</span></p>
    </div>
    <div class="block" style="top:589px;width:225px">
      <h3 class="item">6 Dynamite Burger 6.50</h3>
      <p class="desc">Sweet mayo, Iceberg lettuce, Fried chicken<br>breast, Dynamite sauce , &nbsp;soft deli rolls</p>
    </div>
    <div class="block" style="top:662px;width:225px">
      <h3 class="item">7-Mini fillet Slider</h3>
      <p class="desc">( lemon herbs , Demled peri peri , mangolime)<br>( Mini Fillet , lettus , Cheese , &nbsp;Select your<br>flavoursin a mini bun) <span class="price">4.99</span></p>
    </div>
  </section>
  <div class="photo" role="img" aria-label="Chicken sandwich in a long roll" style="left:546px;top:740px;width:163px;height:86px;border-radius:45%;background:linear-gradient(180deg,#e2b878 0%,#c98a3c 35%,#e9d29a 55%,#6d8a2f 65%,#c88a40 100%)"></div>

  <!-- Sandwich option 2 -->
  <section class="col" style="left:735px;width:220px">
    <p class="col-note" style="left:-5px;width:215px;top:210px;text-align:left">Sandwich &nbsp;All meals servied with chips and dip</p>
    <h2 class="col-title" style="left:0;width:206px;top:226px">Option 2</h2>
    <div class="block" style="top:295px;width:215px">
      <h3 class="step">STEP 1</h3>
      <p class="line">Select your base <span class="price">2.50</span></p>
      <p class="desc" style="margin-top:8px">Brioche bun , soft deli roll , Waffle, double<br>Chesney toasted</p>
    </div>
    <div class="block" style="top:401px;width:215px">
      <h3 class="step">STEP 2</h3>
      <p class="line"><span class="label" style="width:156px">Select your chicken</span><span class="price">3.50</span></p>
      <p class="line">Tenders , chicken breasrt</p>
    </div>
    <div class="block" style="top:471px;width:215px">
      <h3 class="step"><span class="label" style="width:156px">STEP 3</span><span class="price" style="font-weight:400;font-size:9.8px">2.50</span></h3>
      <p class="line">Select your favourite sause</p>
      <p class="line">Classic</p><p class="line">Buffalo</p><p class="line">Bbq</p>
      <p class="line">Mango lime</p><p class="line">Daynmat</p><p class="line">Lemon herbs</p>
      <p class="line">Nashville</p><p class="line">Demless peri peri</p>
    </div>
    <div class="block" style="top:665px;width:215px">
      <h3 class="step">STEP 4</h3>
      <p class="line">Add topping</p><p class="line">Cheese</p><p class="line">Lettuce</p>
      <p class="line">Slaw</p><p class="line">Pickles</p>
    </div>
  </section>
  <div class="photo" role="img" aria-label="Cheesy loaded fries" style="left:842px;top:273px;width:98px;height:56px;border-radius:45%;background:radial-gradient(circle,#f2b533,#d98a1f 60%,transparent 72%)"></div>
  <div class="photo" role="img" aria-label="Sauced chicken wings with dip" style="left:826px;top:534px;width:106px;height:86px;border-radius:45%;background:radial-gradient(circle,#b0482a,#7a2b18 60%,transparent 72%)"></div>
  <div class="photo" role="img" aria-label="Crispy chicken burger with lettuce, tomato and cheese" style="left:790px;top:710px;width:154px;height:124px;border-radius:45% 45% 35% 35%;background:linear-gradient(180deg,#d98a3c 0%,#c7702a 30%,#d4362a 42%,#f2b531 50%,#b3652a 62%,#6aa13a 72%,#d9913f 85%,#c9803a 100%)"></div>

  <!-- Step 5 and sides -->
  <section class="col" style="left:983px;width:210px">
    <div class="block" style="top:218px;width:210px">
      <h3 class="step"><span class="label" style="width:129px">STEP 5</span><span class="price" style="font-weight:400;font-size:9.8px">0.00</span></h3>
      <p class="line">Select your sause</p><p class="line">Blue cheese</p>
      <p class="line">Honey mustard</p><p class="line">House ranch</p>
      <p class="line">Daynmaited</p><p class="line">Tombo's special</p>
    </div>
    <h2 class="col-title" style="left:0;width:195px;top:363px">Sides</h2>
    <div class="block" style="top:402px;width:215px">
      <h3 class="side">1 chicken pop corn &nbsp;5.50</h3>
      <p class="desc">Chicken pop corn topped with meltd<br>cheddar cheese , dynamite sasue , sismes</p>
    </div>
    <div class="block" style="top:472px;width:215px">
      <h3 class="side">2 chilli cheese bites</h3>
      <p class="desc">Chilli cheese bites . Select your dip</p>
    </div>
    <div class="block" style="top:524px;width:215px">
      <h3 class="side">3 Mozerla stick</h3>
    </div>
    <div class="block" style="top:550px;width:215px">
      <h3 class="side">4 Halomi stick</h3>
    </div>
    <div class="block" style="top:576px;width:215px">
      <h3 class="side">5 Garlic mushrooms bites</h3>
    </div>
    <div class="block" style="top:602px;width:215px">
      <h3 class="side">6 Onion rings</h3>
      <p class="desc tight">Mac &amp; cheese bites Tombo's special ( mash<br>potato, &nbsp;grave sause )</p>
      <p class="desc">Honey mustard slaw</p>
    </div>
  </section>
  <div class="photo" role="img" aria-label="Mozzarella sticks with tomato dip" style="left:1068px;top:260px;width:121px;height:81px;border-radius:40%;background:radial-gradient(circle,#e39a45,#c06a28 60%,transparent 72%)"></div>
  <div class="photo" role="img" aria-label="Chicken popcorn in a paper tray" style="left:970px;top:718px;width:218px;height:121px;border-radius:40% 40% 12px 12px;background:linear-gradient(180deg,#e7a54a 0%,#cf8430 55%,#e9e4df 75%,#d23a34 100%)"></div>
</main>
</body>
</html>
```